Packaging Design for Makeup Remover Pads - The winner will do several follow-up products with us

We are building a new brand (Ecological, Young, Friendly, Sustainable, High Quality). We are starting with Makeup Remover Pads. Once the product is launched, other products will follow. We would love to find a designer who does all follow-up designs for us. Our product contains 24 pads with 70% bamboo and 30% cotton. It has 3 layers as a highlight and a free washing bag made of 100% cotton. We would be really happy with a modern, high-quality design. You do not have to invent everything new. Please read the enclosed project description (.pdf file)

Target Market(s)

Women who think sustainably and ecologically

Logo Text

BRIMO TALVE

Colors

Designer to choose colors to be used in the design.

Requirements
Must have
• Our product is% 26quot; premium% 26quot ;. This should be written on the packaging and by a top design. 2 layers of cotton / bamboo. We have 3 layers in top quality. Our package contains 24 pieces, which is more than comparable products have. The whole design should immediately show the customer that it is a sustainable product. It would be great if the logo% 26quot; BRIMO TALVE% 26quot; what a combined word-picture logo. Our first idea is holding hands, or hugging, or holding hands in their hands or holding hands on the earth, or .... This is just to give you a rough idea. Feel free to come up with your own ideas.
Nice to have
• We uploaded a product with a cute panda on the package. An eye-catcher of that kind would be fabulous.

```html
<!DOCTYPE html>
<html lang="en">
<head>
<meta charset="utf-8">
<title>Brimo Talve – Reusable Cleaning Pads</title>
<link href="https://fonts.googleapis.com/css2?family=Montserrat:ital,wght@0,500;0,600;0,700;1,500&display=swap" rel="stylesheet">
<style>
  :root {
    --kraft: #e9bd90;
    --kraft-deep: #d9a877;
    --forest: #4b6b20;
    --forest-soft: #6f8a3e;
    --ink: #3b3a1f;
    --cream: #f3e4c6;
    --white: #ffffff;
  }
  * { margin: 0; padding: 0; box-sizing: border-box; }
  html, body { width: 1200px; height: 690px; overflow: hidden; background: var(--kraft); }
  body { font-family: "Montserrat", sans-serif; color: var(--forest); }
  .package-front { position: relative; width: 1200px; height: 690px; background: var(--kraft); }

  .bamboo-left, .bamboo-right { position: absolute; top: 0; height: 690px; }
  .bamboo-left {
    left: 0; width: 296px;
    background: linear-gradient(90deg, rgba(75,107,32,0.18), rgba(75,107,32,0.05) 70%, rgba(75,107,32,0));
  }
  .bamboo-right {
    right: 0; width: 270px;
    background: linear-gradient(270deg, rgba(200,160,110,0.45), rgba(200,160,110,0.1) 70%, rgba(200,160,110,0));
  }

  .brand-block {
    position: absolute; left: 491px; top: 38px; width: 218px; height: 131px;
    background: var(--forest); border-radius: 16px;
    display: flex; align-items: center; justify-content: center;
  }
  .brand-name {
    font-weight: 600; font-size: 34px; line-height: 1.1; color: var(--cream);
    text-align: center; letter-spacing: 0.5px;
  }

  .product-title { position: absolute; left: 0; width: 1200px; text-align: center; font-weight: 700; }
  .product-title.main { top: 196px; font-size: 62px; letter-spacing: 1px; }
  .product-title.sub { top: 270px; font-size: 38px; font-weight: 600; letter-spacing: 0.5px; }

  .contents-frame {
    position: absolute; left: 385px; top: 343px; width: 432px; height: 201px;
    border: 2px solid var(--white);
  }
  .contents-line {
    position: absolute; left: 0; width: 100%; text-align: center;
    font-style: italic; font-weight: 500; font-size: 24px; color: var(--forest);
  }
  .contents-line.fibre { top: 12px; }
  .contents-line.bag { top: 158px; }
  .wash-bag {
    position: absolute; left: 176px; top: 51px; width: 78px; height: 95px;
    background: linear-gradient(180deg, rgba(75,107,32,0.25), rgba(75,107,32,0.55));
    border-radius: 30px 30px 24px 24px;
  }

  .count-badge { position: absolute; left: 769px; top: 293px; width: 112px; height: 112px; }
  .count-badge svg { position: absolute; inset: 0; }
  .count-text {
    position: absolute; inset: 0; display: flex; flex-direction: column;
    align-items: center; justify-content: center; color: var(--white); font-weight: 700;
  }
  .count-number { font-size: 32px; line-height: 1; }
  .count-unit { font-size: 14px; line-height: 1.2; letter-spacing: 1px; }

  .benefits { position: absolute; top: 571px; left: 0; width: 1200px; }
  .benefit { position: absolute; width: 200px; text-align: center; }
  .benefit svg { display: block; margin: 0 auto; }
  .benefit-label { margin-top: 12px; font-size: 25px; font-weight: 500; color: var(--ink); }
  .benefit.eco { left: 338px; }
  .benefit.sustain { left: 499px; }
  .benefit.reuse { left: 672px; }
</style>
</head>
<body>
<main class="package-front">
  <div class="bamboo-left" role="img" aria-label="Line illustration of bamboo stalks with leaves"></div>
  <div class="bamboo-right" role="img" aria-label="Faint line illustration of bamboo stalks with leaves"></div>

  <div class="brand-block">
    <span class="brand-name">BRIMO<br>TALVE</span>
  </div>

  <h1 class="product-title main">REUSABLE</h1>
  <h2 class="product-title sub">CLEANING PADS</h2>

  <section class="contents-frame">
    <p class="contents-line fibre">70% Bamboo, 30% Cotton</p>
    <div class="wash-bag" role="img" aria-label="Illustration of a cotton mesh wash bag filled with pads"></div>
    <p class="contents-line bag">100% Cotton mesh bag</p>
  </section>

  <div class="count-badge">
    <svg viewBox="0 0 112 112" aria-hidden="true">
      <polygon fill="var(--forest)" points="56,2 65,16 80,8 83,25 100,23 96,40 110,48 98,60 108,74 91,78 92,95 76,91 68,106 56,95 44,106 36,91 20,95 21,78 4,74 14,60 2,48 16,40 12,23 29,25 32,8 47,16"/>
    </svg>
    <div class="count-text">
      <span class="count-number">24</span>
      <span class="count-unit">PADS</span>
    </div>
  </div>

  <ul class="benefits" style="list-style:none">
    <li class="benefit eco">
      <svg width="50" height="50" viewBox="0 0 50 50" aria-hidden="true">
        <circle cx="25" cy="25" r="24" fill="var(--forest)"/>
        <circle cx="25" cy="25" r="13" fill="none" stroke="var(--kraft)" stroke-width="3"/>
      </svg>
      <p class="benefit-label">Eco Friendly</p>
    </li>
    <li class="benefit sustain">
      <svg width="50" height="50" viewBox="0 0 50 50" aria-hidden="true">
        <circle cx="25" cy="25" r="24" fill="var(--forest)"/>
        <path d="M14 32 Q25 36 36 32" fill="none" stroke="var(--kraft)" stroke-width="3" stroke-linecap="round"/>
        <circle cx="25" cy="22" r="5" fill="var(--kraft)"/>
      </svg>
      <p class="benefit-label">Sustainable</p>
    </li>
    <li class="benefit reuse">
      <svg width="50" height="50" viewBox="0 0 50 50" aria-hidden="true">
        <circle cx="25" cy="25" r="24" fill="var(--forest)"/>
        <polygon points="25,12 37,34 13,34" fill="none" stroke="var(--kraft)" stroke-width="3" stroke-linejoin="round"/>
      </svg>
      <p class="benefit-label">Reusable</p>
    </li>
  </ul>
</main>
</body>
</html>
```